Badgerline Custom Woodcraft Website design

Need a small website to showcase my products and take orders

would also like payment options

We do custom wood work along with cnc work in wood plastic and soft metals

we are based in edmonton alberta canada
Updates

Industry/Entity Type

Work

Number of Pages Required

3 page

Requirements
Nice to have
• Interview for for a woodworking magazine
• http://timberquarterlyexample.com/issue-1-02-august-2016/member-spotlight
• I would also like to see metal working/branding iron info
• Also adding the picture of me from the above interview is a nice touch

```html
<!DOCTYPE html>
<html lang="en">
<head>
<meta charset="utf-8">
<title>Badgerline Custom Woodcraft</title>
<link rel="stylesheet" href="https://fonts.googleapis.com/css2?family=Lato:wght@300;400;700;900&display=swap">
<style>
:root{
  --ink:#1e1e1e;
  --muted:#8a8a8a;
  --hero-bg:#e6e6e6;
  --card-bg:#e8e8e8;
  --bar:#333333;
  --brown:#705248;
  --brown-dark:#4f3a33;
  --tan:#b58f74;
  --accent:#b98262;
  --white:#ffffff;
}
*{box-sizing:border-box;margin:0;padding:0}
html,body{width:1200px;height:2261px;overflow:hidden;background:var(--white);font-family:"Lato",sans-serif;color:var(--ink)}
.page{position:relative;width:1200px;height:2261px}

/* header */
.site-header{position:absolute;top:0;left:0;width:1200px;height:105px;background:var(--white)}
.brand{position:absolute;left:78px;top:30px;display:flex;align-items:center;gap:14px}
.brand-mark{width:46px;height:46px;border-radius:50%;background:var(--ink)}
.brand-name{font-size:27px;font-weight:400;color:var(--brown);letter-spacing:1px;line-height:1}
.header-tools{position:absolute;right:0;top:0;display:flex;height:105px}
.tool{width:104px;height:105px;display:flex;align-items:center;justify-content:center}
.tool:nth-child(1){background:#f6f6f6}
.tool:nth-child(2){background:#efefef}
.tool:nth-child(3){background:#e9e9e9}
.tool:nth-child(4){background:#e2e2e2}

/* hero */
.hero{position:absolute;top:105px;left:0;width:1200px;height:572px;background:var(--hero-bg)}
.hero-title{position:absolute;left:79px;top:198px;font-weight:300;font-size:72px;line-height:83px;color:var(--ink)}
.hero-dots{position:absolute;left:77px;top:506px;display:flex;gap:20px}
.hero-dot{width:21px;height:21px;border:1.5px solid #555;border-radius:50%;position:relative}
.hero-dot.is-active::after{content:"";position:absolute;inset:4px;border-radius:50%;background:#555}
.hero-product{position:absolute;left:761px;top:76px;width:317px;height:422px;border-radius:50%;background:radial-gradient(ellipse at 45% 40%,#6e4a57,#4a2f38 70%,#3a262b)}
.hero-shadow{position:absolute;left:790px;top:478px;width:260px;height:30px;border-radius:50%;background:radial-gradient(ellipse,rgba(0,0,0,.22),rgba(0,0,0,0) 70%)}

/* sections */
.section-title{position:absolute;left:80px;font-weight:300;font-size:41px;letter-spacing:.5px;color:var(--ink)}
.products-title{top:724px}
.about-title{top:1528px}

.product-grid{position:absolute;left:77px;top:791px;display:grid;grid-template-columns:repeat(3,333px);grid-auto-rows:334px;column-gap:22px;row-gap:21px}
.product-card{position:relative;background:var(--card-bg);overflow:hidden}
.product-photo{position:absolute;left:50%;transform:translateX(-50%);top:40px;width:200px;height:170px;border-radius:6px}
.product-info{position:absolute;left:23px;right:23px;bottom:22px;display:flex;justify-content:space-between;align-items:flex-end}
.product-name{font-size:17px;color:var(--ink);line-height:22px}
.product-sub{font-size:15px;color:var(--muted);line-height:20px}
.product-order{text-align:right;font-size:14px;line-height:22px}
.product-price{font-weight:700;font-size:14px}
.product-card.is-hover .product-info{bottom:65px}
.view-detail{position:absolute;left:0;bottom:0;width:100%;height:43px;background:var(--bar);color:var(--white);font-size:14px;display:flex;align-items:center;justify-content:center;letter-spacing:.5px}

/* about */
.about-feature{position:absolute;left:77px;top:1593px;width:1045px;height:365px;overflow:hidden}
.about-photo-left{position:absolute;inset:0;background:linear-gradient(160deg,#e9e6e1 0%,#d9c8b4 45%,#c7b29a 100%)}
.about-photo-right{position:absolute;inset:0;background:linear-gradient(180deg,#7a5b3f 0%,#5c4330 60%,#3e2d22 100%);clip-path:polygon(812px 0,1045px 0,1045px 365px,616px 365px)}
.about-caption{position:absolute;left:0;bottom:0;width:297px;height:144px;background:var(--white);padding:24px 22px}
.caption-date{font-size:12px;color:#555}
.caption-title{font-size:18px;color:#444;margin-top:8px}
.caption-dots{position:absolute;left:22px;bottom:20px;display:flex;gap:11px}
.caption-dot{width:9px;height:9px;border-radius:50%;background:#d4d4d4}
.caption-dot.is-active{background:#9a9a9a}
.spotlight-heading{position:absolute;left:680px;width:370px;top:254px;text-align:center;font-weight:700;font-size:39px;line-height:42px;color:var(--white);text-shadow:0 2px 4px rgba(0,0,0,.45)}

/* footer */
.site-footer{position:absolute;left:0;top:2053px;width:1200px;height:208px;background:var(--brown)}
.footer-badge{position:absolute;left:551px;top:2003px;width:104px;height:104px;border-radius:50%;background:var(--white);display:flex;align-items:center;justify-content:center}
.footer-badge span{display:block;width:84px;height:84px;border-radius:50%;background:#e6c9ae}
.footer-nav{position:absolute;left:80px;top:30px;display:flex;gap:0;font-size:16px}
.footer-nav a{text-decoration:none;color:var(--tan);margin-right:47px}
.footer-nav a.is-current{color:var(--white)}
.social{position:absolute;left:931px;top:20px;display:flex;gap:10px}
.social-item{width:41px;height:41px;border-radius:50%;border:2px solid var(--white)}
.social-item.is-filled{background:var(--white)}
.footer-rule{position:absolute;left:77px;top:82px;width:1045px;height:1px;background:rgba(255,255,255,.3)}
.contact{position:absolute;top:105px;display:flex;align-items:center;gap:14px;color:var(--white);font-size:14px;line-height:18px}
.contact-icon{width:46px;height:46px;border-radius:50%;background:var(--brown-dark);display:flex;align-items:center;justify-content:center}
.contact strong{display:block;font-weight:700;font-size:13px}
.contact-address{left:77px}
.contact-phone{left:517px}
.contact-email{left:869px}
.copyright{position:absolute;left:0;width:100%;top:174px;text-align:center;color:var(--white);font-weight:700;font-size:14px}
.copyright .accent{color:var(--accent)}
</style>
</head>
<body>
<div class="page">

  <header class="site-header">
    <div class="brand">
      <span class="brand-mark"></span>
      <span class="brand-name">BADGERLINE CUSTOM WOODCRAFT</span>
    </div>
    <nav class="header-tools">
      <div class="tool" aria-label="Menu">
        <svg width="20" height="16" viewBox="0 0 20 16"><rect y="0" width="20" height="3" fill="#222"/><rect y="6.5" width="20" height="3" fill="#222"/><rect y="13" width="20" height="3" fill="#222"/></svg>
      </div>
      <div class="tool" aria-label="Search">
        <svg width="18" height="18" viewBox="0 0 18 18"><circle cx="7.5" cy="7.5" r="5.5" fill="none" stroke="#222" stroke-width="2.5"/><line x1="11.5" y1="11.5" x2="16.5" y2="16.5" stroke="#222" stroke-width="3" stroke-linecap="round"/></svg>
      </div>
      <div class="tool" aria-label="Account">
        <svg width="16" height="18" viewBox="0 0 16 18"><circle cx="8" cy="5" r="4.5" fill="#222"/><path d="M0 18 Q0 10 8 10 Q16 10 16 18 Z" fill="#222"/></svg>
      </div>
      <div class="tool" aria-label="Basket">
        <svg width="22" height="18" viewBox="0 0 22 18"><path d="M1 6 H21 L18.5 17 H3.5 Z" fill="none" stroke="#222" stroke-width="2" stroke-linejoin="round"/><path d="M6 6 L10 1 M16 6 L12 1" stroke="#222" stroke-width="2" stroke-linecap="round"/><line x1="8" y1="9" x2="8" y2="14" stroke="#222" stroke-width="1.6"/><line x1="11" y1="9" x2="11" y2="14" stroke="#222" stroke-width="1.6"/><line x1="14" y1="9" x2="14" y2="14" stroke="#222" stroke-width="1.6"/></svg>
      </div>
    </nav>
  </header>

  <section class="hero">
    <h1 class="hero-title">African Mahogany<br>Cribbage Board</h1>
    <div class="hero-dots">
      <span class="hero-dot"></span>
      <span class="hero-dot"></span>
      <span class="hero-dot is-active"></span>
    </div>
    <div class="hero-shadow"></div>
    <div class="hero-product" role="img" aria-label="Oval mahogany cribbage board with a carved eagle head"></div>
  </section>

  <h2 class="section-title products-title">OUR PRODUCTS</h2>
  <div class="product-grid">
    <article class="product-card is-hover">
      <div class="product-photo" role="img" aria-label="Wooden wrench-shaped bottle opener" style="top:30px;height:120px;background:linear-gradient(135deg,#e2c29c,#c89b6c)"></div>
      <div class="product-info">
        <div><div class="product-name">Lorem ipsum is...</div><div class="product-sub">simply dummy text</div></div>
        <div class="product-order">ORDER NOW<div class="product-price">48.60 $</div></div>
      </div>
      <div class="view-detail">VIEW DETAIL</div>
    </article>
    <article class="product-card">
      <div class="product-photo" role="img" aria-label="Pine dartboard cabinet with open doors" style="background:linear-gradient(90deg,#c98a3c,#e9b25f 30%,#2a2a2a 45%,#2a2a2a 60%,#e9b25f 75%,#c98a3c)"></div>
      <div class="product-info">
        <div><div class="product-name">Lorem ipsum is...</div><div class="product-sub">simply dummy text</div></div>
        <div class="product-order">ORDER NOW<div class="product-price">48.60 $</div></div>
      </div>
    </article>
    <article class="product-card">
      <div class="product-photo" role="img" aria-label="Folding wooden camp stool" style="background:linear-gradient(180deg,#d8b48a,#b98a5c)"></div>
      <div class="product-info">
        <div><div class="product-name">Lorem ipsum is...</div><div class="product-sub">simply dummy text</div></div>
        <div class="product-order">ORDER NOW<div class="product-price">48.60 $</div></div>
      </div>
    </article>
    <article class="product-card">
      <div class="product-photo" role="img" aria-label="Carved wooden dolphin ornament" style="top:70px;width:260px;height:100px;background:linear-gradient(90deg,#a44d26,#7f3617)"></div>
      <div class="product-info">
        <div><div class="product-name">Lorem ipsum is...</div><div class="product-sub">simply dummy text</div></div>
        <div class="product-order">ORDER NOW<div class="product-price">48.60 $</div></div>
      </div>
    </article>
    <article class="product-card">
      <div class="product-photo" role="img" aria-label="Engraved metal plaque with a barn scene" style="top:38px;width:194px;height:186px;background:linear-gradient(135deg,#d9d9d9,#9c9c9c 55%,#c4c4c4)"></div>
      <div class="product-info">
        <div><div class="product-name">Lorem ipsum is...</div><div class="product-sub">simply dummy text</div></div>
        <div class="product-order">ORDER NOW<div class="product-price">48.60 $</div></div>
      </div>
    </article>
    <article class="product-card">
      <div class="product-photo" role="img" aria-label="Carved wooden bulldog head wearing a hat" style="background:linear-gradient(180deg,#b36c4c,#8a4a2e)"></div>
      <div class="product-info">
        <div><div class="product-name">Lorem ipsum is...</div><div class="product-sub">simply dummy text</div></div>
        <div class="product-order">ORDER NOW<div class="product-price">48.60 $</div></div>
      </div>
    </article>
  </div>

  <h2 class="section-title about-title">ABOUT</h2>
  <section class="about-feature">
    <div class="about-photo-left" role="img" aria-label="Rotary tool carving a light wood panel"></div>
    <div class="about-photo-right" role="img" aria-label="Dale Mercer standing in his workshop"></div>
    <div class="spotlight-heading">Member Spotlight:<br>Dale Mercer</div>
    <div class="about-caption">
      <div class="caption-date">August 2016</div>
      <div class="caption-title">Member Spotlight: Dale Mercer</div>
      <div class="caption-dots">
        <span class="caption-dot"></span><span class="caption-dot"></span><span class="caption-dot"></span><span class="caption-dot is-active"></span>
      </div>
    </div>
  </section>

  <footer class="site-footer">
    <nav class="footer-nav">
      <a class="is-current" href="#">Home</a>
      <a href="#">About Us</a>
      <a href="#">Products</a>
      <a href="#">Contact Us</a>
    </nav>
    <div class="social">
      <span class="social-item is-filled"></span>
      <span class="social-item"></span>
      <span class="social-item"></span>
      <span class="social-item"></span>
    </div>
    <div class="footer-rule"></div>
    <div class="contact contact-address">
      <span class="contact-icon"><svg width="14" height="20" viewBox="0 0 14 20"><path d="M7 0 C3 0 0 3 0 7 C0 12 7 20 7 20 C7 20 14 12 14 7 C14 3 11 0 7 0 Z" fill="#fff"/><circle cx="7" cy="7" r="2.6" fill="#4f3a33"/></svg></span>
      <div><strong>POSTAL ADDRESS</strong>123 Building Name, City, Country - zipcode</div>
    </div>
    <div class="contact contact-phone">
      <span class="contact-icon"><svg width="18" height="18" viewBox="0 0 18 18"><path d="M3.5 1 L6.5 1 L8 5 L6 6.5 C7 9 9 11 11.5 12 L13 10 L17 11.5 L17 14.5 C17 16 16 17 14.5 17 C7 17 1 11 1 3.5 C1 2 2 1 3.5 1 Z" fill="#fff"/></svg></span>
      <div>123 - 4567 - 890</div>
    </div>
    <div class="contact contact-email">
      <span class="contact-icon"><svg width="18" height="14" viewBox="0 0 18 14"><rect width="18" height="14" rx="1.5" fill="#fff"/><path d="M1 1.5 L9 8 L17 1.5" fill="none" stroke="#4f3a33" stroke-width="1.6"/></svg></span>
      <div>info@badgerline.cw</div>
    </div>
    <div class="copyright">© <span class="accent">BADGERLINE CUSTOM WOODCRAFT</span> - 2016. All Rights Reserved</div>
  </footer>
  <div class="footer-badge"><span></span></div>

</div>
</body>
</html>
```